Copperline Structural Roof Inc.

We need a business card design for a commercial roofing company metro Boston based. We are a roofing company that help people manage buildings and build relationships with clients. We would like a unique card that stands out. We want a business card with a white background. We do not want a roof as the logo.

Industry/Entity Type

Roofing

```html
<!DOCTYPE html>
<html lang="en">
<head>
<meta charset="utf-8">
<title>Copperline Structural Roof Inc. – Business Card</title>
<link rel="stylesheet" href="https://fonts.googleapis.com/css2?family=Cinzel:wght@700&family=Tinos:wght@400&display=swap">
<style>
  :root {
    --navy: #0a2d7a;
    --navy-deep: #062266;
    --sky: #0a78c8;
    --ink: #1f3f86;
    --grey: #7c8597;
    --paper: #ffffff;
    --stage: #e9ecf0;
  }
  * { margin: 0; padding: 0; box-sizing: border-box; }
  html, body { width: 1200px; height: 900px; overflow: hidden; background: var(--stage); }
  .canvas { position: relative; width: 1200px; height: 900px; }
  .card {
    position: absolute; left: 290px; width: 620px; height: 354px;
    background: var(--paper); overflow: hidden;
    box-shadow: 0 10px 28px rgba(20, 35, 70, 0.14);
  }
  .card--back { top: 66px; }
  .card--front { top: 480px; }
  .card__bands { position: absolute; inset: 0; width: 620px; height: 354px; }

  .wordmark {
    position: absolute; left: 0; right: 0; top: 118px;
    display: flex; align-items: center; justify-content: center; gap: 16px;
  }
  .wordmark__square { width: 26px; height: 26px; background: var(--navy); }
  .wordmark__name {
    font-family: "Cinzel", serif; font-weight: 700; font-size: 25px;
    letter-spacing: 2px; color: var(--navy); line-height: 1.15;
  }

  .website {
    position: absolute; display: flex; align-items: center; gap: 9px;
    font-family: "Tinos", serif; font-size: 17px; color: var(--paper);
  }
  .card--back .website { right: 44px; bottom: 30px; }
  .card--front .website { right: 44px; bottom: 48px; }

  .person { position: absolute; left: 48px; top: 58px; }
  .person__name {
    font-family: "Cinzel", serif; font-weight: 700; font-size: 27px;
    color: var(--sky); letter-spacing: 1px; line-height: 1;
  }
  .person__title {
    font-family: "Cinzel", serif; font-weight: 700; font-size: 16px;
    color: var(--grey); letter-spacing: 1.5px; margin: 6px 0 0 26px;
  }
  .contact { list-style: none; margin: 18px 0 0 26px; font-family: "Tinos", serif; font-size: 16px; color: var(--ink); line-height: 1.3; }
  .contact__row { display: flex; align-items: flex-start; gap: 10px; }
  .contact__icon { width: 14px; height: 14px; margin-top: 3px; flex: none; }
  .contact__row--gap { margin-top: 6px; }
</style>
</head>
<body>
<main class="canvas">

  <section class="card card--back" aria-label="Card back">
    <svg class="card__bands" viewBox="0 0 620 354" aria-hidden="true">
      <path d="M0 300 L0 354 L620 354 L620 270 L380 270 C360 270 358 300 336 300 Z" fill="var(--navy)"/>
    </svg>
    <div class="wordmark">
      <span class="wordmark__square"></span>
      <span class="wordmark__name">Copperline<br>Structural Roof Inc.</span>
    </div>
    <p class="website">
      <svg width="14" height="14" viewBox="0 0 14 14" aria-hidden="true"><circle cx="7" cy="7" r="6" fill="none" stroke="#fff" stroke-width="1.3"/><path d="M1 7h12M7 1c-3 3.5-3 8.5 0 12M7 1c3 3.5 3 8.5 0 12" fill="none" stroke="#fff" stroke-width="1"/></svg>
      www.copperline.com
    </p>
  </section>

  <section class="card card--front" aria-label="Card front">
    <svg class="card__bands" viewBox="0 0 620 354" aria-hidden="true">
      <path d="M0 322 L620 322 L620 354 L0 354 Z" fill="var(--sky)"/>
      <path d="M300 322 C322 322 324 278 346 278 L620 278 L620 322 Z" fill="var(--navy)"/>
    </svg>
    <div class="person">
      <h1 class="person__name">Marco Delgado</h1>
      <p class="person__title">President</p>
      <ul class="contact">
        <li class="contact__row">
          <svg class="contact__icon" viewBox="0 0 14 14" aria-hidden="true"><path d="M7 1a4 4 0 0 1 4 4c0 3-4 8-4 8S3 8 3 5a4 4 0 0 1 4-4z" fill="var(--ink)"/><circle cx="7" cy="5" r="1.5" fill="#fff"/></svg>
          <span>48 Harbor Row, Quincy, MA<br>USA 02169</span>
        </li>
        <li class="contact__row contact__row--gap">
          <svg class="contact__icon" viewBox="0 0 14 14" aria-hidden="true"><path d="M1 5c0-2 2-3 6-3s6 1 6 3l-3 1-1-2H5L4 6zM3 7h8l1 5H2z" fill="var(--ink)"/></svg>
          <span>(+1) 617 555 0142</span>
        </li>
        <li class="contact__row">
          <svg class="contact__icon" viewBox="0 0 14 14" aria-hidden="true"><rect x="3" y="1" width="8" height="5" fill="none" stroke="var(--ink)" stroke-width="1.3"/><rect x="1" y="6" width="12" height="6" fill="var(--ink)"/></svg>
          <span>(+1) 617 555 0143</span>
        </li>
        <li class="contact__row">
          <svg class="contact__icon" viewBox="0 0 14 14" aria-hidden="true"><rect x="1" y="3" width="12" height="8" fill="none" stroke="var(--ink)" stroke-width="1.3"/><path d="M1 3l6 5 6-5" fill="none" stroke="var(--ink)" stroke-width="1.3"/></svg>
          <span>hello@copperline.com</span>
        </li>
      </ul>
    </div>
    <p class="website">
      <svg width="14" height="14" viewBox="0 0 14 14" aria-hidden="true"><circle cx="7" cy="7" r="6" fill="none" stroke="#fff" stroke-width="1.3"/><path d="M1 7h12M7 1c-3 3.5-3 8.5 0 12M7 1c3 3.5 3 8.5 0 12" fill="none" stroke="#fff" stroke-width="1"/></svg>
      www.copperline.com
    </p>
  </section>

</main>
</body>
</html>
```